Modern, eye catching eliquid bottle label. 1.5 x 2.75

We need a label design for our e-juice bottles. The labels to be printed are 1.5 inches in height and 2.75 inches in width. We are looking to include our website (www.quillbrookmistparlor.com) and our phone number of 2 different shops. The most prominent thing needs to be our logo(attached .pdf and jpeg). We will need 2 spots that we can edit on an ongoing basis for nicotine strength and the flavor. We want something simplistic but eye-catching. Our colors are Purple, Red, and Orange. We would also like our website fairly prominent as well.

Target Market(s)

18-45 vapers and e-cigarette users

Font styles to use
Serif

Colors
6b449b
f78e1f
ec1f27
ffffff
000000

Requirements
Must have
• eye catching
• "Quillbrook Mist" must be LARGE
• phone number
• website
• areas for flavor name and nicotine strength
• orange, purple, black and red
Nice to have
• clean, abstract vectors
• "corporate look"
• think of a DUNTRA FIZZ can, you immediately know what your'e looking at.
• Our V in vapor is our go to logo
Should not have
• no grunge effects
• no round shapes

```html
<!DOCTYPE html>
<html lang="en">
<head>
<meta charset="utf-8">
<title>Quillbrook Mist – E-Liquid Label</title>
<link rel="stylesheet" href="https://fonts.googleapis.com/css2?family=Pathway+Gothic+One&family=Allura&family=Open+Sans:wght@400&display=swap">
<style>
  :root {
    --purple: #6b449b;
    --purple-light: #8a3fd0;
    --purple-deep: #5a2a9a;
    --orange: #f78e1f;
    --red: #ec1f27;
    --white: #ffffff;
    --black: #000000;
  }
  html, body {
    margin: 0;
    width: 1200px;
    height: 1200px;
    overflow: hidden;
    background: var(--white);
  }
  .label {
    position: absolute;
    left: 50px;
    top: 297px;
    width: 1100px;
    height: 605px;
    display: flex;
    gap: 5px;
    background: var(--white);
    box-shadow: 0 3px 8px rgba(0,0,0,0.35);
    font-family: "Pathway Gothic One", "Arial Narrow", sans-serif;
    color: var(--white);
  }
  .panel {
    position: relative;
    height: 100%;
    box-sizing: border-box;
  }
  .panel-side {
    background: linear-gradient(180deg, var(--orange) 0%, #f0612a 45%, var(--red) 100%);
  }
  .panel-info { width: 272px; font-size: 35px; line-height: 40px; }
  .panel-legal { width: 298px; font-size: 32px; line-height: 33px; }
  .panel-brand {
    flex: 1;
    background: radial-gradient(ellipse at 60% 40%, var(--purple-light) 0%, var(--purple-deep) 70%, var(--purple) 100%);
  }
  .panel p { margin: 0; }
  .panel-info .block { position: absolute; left: 30px; }
  .nicotine { top: 46px; }
  .other-flavours { top: 179px; }
  .other-flavours ul { list-style: none; margin: 22px 0 0; padding: 0; }
  .dates { top: 474px; }
  .dates p + p { margin-top: 8px; }
  .panel-legal .block { position: absolute; left: 20px; right: 10px; }
  .warning { top: 42px; }
  .ingredients { top: 256px; }
  .locations { top: 476px; }
  .locations p + p { margin-top: 14px; }
  .logo-badge {
    position: absolute;
    left: 50%;
    top: 33px;
    transform: translateX(-50%);
    width: 420px;
    height: 250px;
  }
  .logo-badge svg { position: absolute; inset: 0; }
  .brand-name {
    position: absolute;
    inset: 0;
    display: flex;
    align-items: center;
    justify-content: center;
    font-size: 62px;
    color: var(--purple);
    letter-spacing: 1px;
  }
  .flavour-name {
    position: absolute;
    top: 292px;
    left: 0;
    right: 0;
    text-align: center;
    font-family: "Allura", cursive;
    font-weight: 400;
    font-size: 128px;
    line-height: 128px;
    margin: 0;
  }
  .specs {
    position: absolute;
    top: 457px;
    left: 78px;
    right: 90px;
    height: 60px;
    border-top: 1px solid rgba(255,255,255,0.55);
    border-bottom: 1px solid rgba(255,255,255,0.55);
    display: flex;
    justify-content: space-between;
    align-items: center;
    padding: 0 6px;
    font-family: "Open Sans", Arial, sans-serif;
    font-size: 29px;
    line-height: 1;
  }
  .website {
    position: absolute;
    top: 536px;
    left: 0;
    right: 0;
    text-align: center;
    font-size: 33px;
    line-height: 40px;
  }
</style>
</head>
<body>
  <section class="label" aria-label="E-liquid bottle label">
    <div class="panel panel-side panel-info">
      <p class="block nicotine">Nicotine Level</p>
      <div class="block other-flavours">
        <p>Other Flavours:</p>
        <ul>
          <li>Sample Flavour1</li>
          <li>Sample Flavour2</li>
          <li>Sample Flavour3</li>
          <li>Sample Flavour4</li>
        </ul>
      </div>
      <div class="block dates">
        <p>Mfg Date:</p>
        <p>Exp Date:</p>
      </div>
    </div>

    <div class="panel panel-brand">
      <div class="logo-badge">
        <svg width="420" height="250" viewBox="0 0 420 250" aria-hidden="true">
          <defs>
            <radialGradient id="badgeFill" cx="50%" cy="40%" r="60%">
              <stop offset="0%" stop-color="#ffffff"/>
              <stop offset="100%" stop-color="#e9e9ee"/>
            </radialGradient>
          </defs>
          <ellipse cx="210" cy="125" rx="208" ry="123" fill="url(#badgeFill)"/>
        </svg>
        <div class="brand-name">Quillbrook Mist</div>
      </div>
      <h1 class="flavour-name">Flavour</h1>
      <div class="specs">
        <span class="strength">06mg</span>
        <span class="volume">15ml</span>
      </div>
      <div class="website">www.quillbrookmistparlor.com</div>
    </div>

    <div class="panel panel-side panel-legal">
      <p class="block warning">Warning: Please keep<br>out of children's reach;<br>keep in a cool, dark place<br>or in the refrigerator for<br>extended life;</p>
      <p class="block ingredients">Ingredients:<br>USP Glycerine, USP<br>Propylene Glycol,<br>Natural and Artificial<br>Flavoring</p>
      <div class="block locations">
        <p>Location 1: 214-555-0187</p>
        <p>Location 2: 214-555-0187</p>
      </div>
    </div>
  </section>
</body>
</html>
```